Harborline Cover Stationary Design

We require stationary design for a new Life Insurance Business, Harborline Cover based in Melbourne Australia.
The logo for this business was successfully developed using Pixel Forum (refer attached) and all stationary will incorporate this logo design.
The layout of the stationary needs to be clear, modern and of a premium quality.
The colours to be incorporated are to be the same as those in the logo, as well as black.
Stationary required:
1) Business Card
2) Letter Head
3) With Compliments Slip
4) Envelope (both A4 and DL size)
Updates
Thanks to everyone who has submitted a design.
Hi all,
Industry/Entity Type
Business
Requirements
Must have
- For the Business Card - on front:
Company Logo: refer attached
Dorian Velk
CFP, BBUS (Acc), CA
Director
417 Marlow Parade, Kestwick, VIC 3472
T: 03 9647 2250
F: 03 9682 4037
M: 0400 917 356
email: dvelk@harborlinecover.example.au
Harborline Cover Pty Ltd trading as Harborline Cover is an Authorised Representative of QRT Wealth Advisory Pty Limited (this should be at the bottom of the business card and in very small font)
Background colour on card should be white.
For the Business Card -on back:
Company Logo. The Symbol within the logo could be bigger than the text.
www.harborlinecover.example.au
Background for the back of the card could be in either Black or white.
For the Letterhead & With Compliments Slip:
T: 03 9647 2250
F: 03 9682 4037
M: 0400 917 356
E: dvelk@harborlinecover.example.au
W: www.harborlinecover.example.au
Harborline Cover Pty Ltd trading as Harborline Cover is an Authorised Representative of QRT Wealth Advisory Pty Limited ABN 46 173 509 862 AFSL No. 518904 (this should be at the bottom/footer and be in a very small font)
Envelopes:
Other Must Haves:
Choices of Font Type and Colour should be relatively consistent across each item of stationary.
There should also be consistency in the font size for the Letterhead and With Compliments Slip.

```html
<!DOCTYPE html>
<html lang="en">
<head>
<meta charset="utf-8">
<title>Harborline Cover Stationery</title>
<link rel="stylesheet" href="https://fonts.googleapis.com/css2?family=Josefin+Sans:wght@400;600;700&display=swap">
<style>
  :root {
    --backdrop: #e8e5e0;
    --paper: #ffffff;
    --ink-black: #141516;
    --brand-green: #9cc534;
    --text-green: #8bbd2c;
    --brand-grey: #8f9092;
    --pale-green: #dbe9bd;
    --pale-grey: #d6d6d8;
    --edge: #b9b6b0;
  }
  * { margin: 0; padding: 0; box-sizing: border-box; }
  html, body { width: 1200px; height: 687px; overflow: hidden; }
  body {
    position: relative;
    background: var(--backdrop);
    font-family: "Josefin Sans", "Trebuchet MS", sans-serif;
    color: var(--text-green);
  }
  .piece { position: absolute; background: var(--paper); border: 1px solid var(--edge); overflow: hidden; }

  .wordmark {
    display: inline-flex; align-items: center; gap: 0.35em;
    font-weight: 600; color: var(--brand-grey); white-space: nowrap; line-height: 1;
    letter-spacing: 0.02em;
  }
  .wordmark .mark-dot {
    width: 0.9em; height: 0.9em; border-radius: 50%; background: var(--brand-green); flex: none;
  }

  .symbol-field {
    position: absolute;
    background: radial-gradient(circle at 70% 40%, var(--pale-green) 0%, var(--pale-grey) 55%, rgba(255,255,255,0) 80%);
  }
  .symbol-field.on-dark {
    background: radial-gradient(circle at 65% 55%, #6f8f2a 0%, #4d4f52 50%, rgba(20,21,22,0) 80%);
  }

  /* Envelope, A4 green */
  .envelope-a4 { left: 60px; top: 356px; width: 412px; height: 179px; background: var(--brand-green); }
  .envelope-a4 .flap { position: absolute; left: 0; top: 0; width: 100%; height: 57px; }
  .envelope-a4 .wordmark { position: absolute; left: 135px; top: 16px; font-size: 16px; }

  /* Envelope, DL white */
  .envelope-dl { left: 342px; top: 450px; width: 412px; height: 179px; }
  .envelope-dl .wordmark { position: absolute; left: 22px; top: 34px; font-size: 17px; }
  .envelope-dl .return-address { position: absolute; right: 14px; bottom: 11px; font-size: 10.5px; font-weight: 600; }

  /* Business card, dark front */
  .card-dark { left: 599px; top: 143px; width: 153px; height: 88px; background: var(--ink-black); border-color: #333; }
  .card-dark .wordmark { position: absolute; left: 8px; top: 9px; font-size: 6px; color: var(--pale-grey); }
  .card-dark .holder { position: absolute; left: 104px; top: 10px; font-size: 3.6px; line-height: 1.5; font-weight: 600; color: var(--brand-green); }
  .card-dark .contact { position: absolute; left: 8px; top: 61px; font-size: 3.4px; line-height: 1.5; font-weight: 600; color: var(--brand-green); }
  .card-dark .symbol-field { right: 0; bottom: 0; width: 52px; height: 52px; }

  /* Business card, white back */
  .card-back { left: 599px; top: 246px; width: 153px; height: 87px; }
  .card-back .symbol-field.top-left { left: -6px; top: -6px; width: 50px; height: 40px; }
  .card-back .symbol-field.right { right: -4px; top: 30px; width: 46px; height: 50px; }
  .card-back .wordmark { position: absolute; left: 47px; top: 39px; font-size: 6.5px; }
  .card-back .website { position: absolute; left: 8px; bottom: 5px; font-size: 4.6px; letter-spacing: 0.12em; font-weight: 600; }

  /* Business card, white front */
  .card-front { left: 601px; top: 348px; width: 152px; height: 87px; }
  .card-front .wordmark { position: absolute; right: 8px; top: 6px; font-size: 5.5px; }
  .card-front .contact { position: absolute; left: 5px; top: 60px; font-size: 3.4px; line-height: 1.45; font-weight: 600; }

  /* Letterhead */
  .letterhead { left: 777px; top: 62px; width: 360px; height: 508px; }
  .letterhead .wordmark { position: absolute; left: 24px; top: 31px; font-size: 17px; }
  .letterhead .contact { position: absolute; left: 13px; top: 425px; font-size: 9.4px; line-height: 1.42; font-weight: 600; letter-spacing: 0.02em; }
  .letterhead .symbol-field { right: 0; bottom: 0; width: 160px; height: 172px; }
</style>
</head>
<body>

  <section class="piece envelope-a4" aria-label="A4 envelope">
    <svg class="flap" viewBox="0 0 412 57" preserveAspectRatio="none" aria-hidden="true">
      <polygon points="0,0 412,0 392,57 20,57" fill="#ffffff" stroke="#8a9a4a" stroke-width="0.8"/>
    </svg>
    <div class="wordmark"><span class="mark-dot"></span>Harborline Cover</div>
  </section>

  <section class="piece envelope-dl" aria-label="DL envelope">
    <div class="wordmark"><span class="mark-dot"></span>Harborline Cover</div>
    <p class="return-address">417 Marlow Parade, Kestwick, VIC 3472</p>
  </section>

  <section class="piece card-dark" aria-label="Business card front">
    <div class="wordmark"><span class="mark-dot"></span>Harborline Cover</div>
    <div class="holder">
      <p>Dorian Velk</p>
      <p>CFP, BBUS (Acc), CA</p>
      <p>Director</p>
    </div>
    <div class="contact">
      <p>417 Marlow Parade, Kestwick, VIC 3472</p>
      <p>T: 03 9647 2250</p>
      <p>F: 03 9682 4037</p>
      <p>M: 0400 917 356</p>
      <p>email: dvelk@harborlinecover.example.au</p>
    </div>
    <div class="symbol-field on-dark" role="img" aria-label="Enlarged brand symbol decoration"></div>
  </section>

  <section class="piece card-back" aria-label="Business card back">
    <div class="symbol-field top-left" role="img" aria-label="Brand symbol decoration"></div>
    <div class="symbol-field right" role="img" aria-label="Brand symbol decoration"></div>
    <div class="wordmark"><span class="mark-dot"></span>Harborline Cover</div>
    <p class="website">www.harborlinecover.example.au</p>
  </section>

  <section class="piece card-front" aria-label="Business card front, white">
    <div class="wordmark"><span class="mark-dot"></span>Harborline Cover</div>
    <div class="contact">
      <p>417 Marlow Parade, Kestwick, VIC 3472</p>
      <p>T: 03 9647 2250</p>
      <p>F: 03 9682 4037</p>
      <p>M: 0400 917 356</p>
      <p>email: dvelk@harborlinecover.example.au</p>
      <p>website: www.harborlinecover.example.au</p>
    </div>
  </section>

  <section class="piece letterhead" aria-label="Letterhead">
    <div class="wordmark"><span class="mark-dot"></span>Harborline Cover</div>
    <div class="contact">
      <p>417 Marlow Parade, Kestwick, VIC 3472</p>
      <p>T: 03 9647 2250</p>
      <p>F: 03 9682 4037</p>
      <p>M: 0400 917 356</p>
      <p>email: dvelk@harborlinecover.example.au</p>
      <p>website www.harborlinecover.example.au</p>
    </div>
    <div class="symbol-field" role="img" aria-label="Large faint brand symbol decoration"></div>
  </section>

</body>
</html>
```